Business Plan for Bourbon and Music Festival

I will create the verbiage for a 5 page business plan for a bourbon and music festival to be held at Wrenhill Acres in Louisville, Kentucky. This document will outline the plan to stage a festival. I have and will continue to edit the narrative used in the document. I just need the plan to be presented in a professional looking business plan with images that will convey the festival atmosphere I am looking to create. I have created a map of where I want to stage the festival but will probably need a better map showing where the festival will be held as well as pictures of Wrenhill Acres and other pictures that will describe the site and opportunity.

Target Market(s)

The document will be used to market the festival to borboun producers, musicians, chefs, music promoters and other people needed to stage a music festival.

Industry/Entity Type

Business

Font styles to use
Serif

Colors
33b8a4
87cfc6
cadf82
85cae6

Requirements
Must have
• The package must have a sleek look that conveys the potential success of a bourbon/music festival. It must include pictures of bourbon, music festivals, images of Wrenhill Acres, a map of the area and also a general grapic theme to be used throughout the document.

```html
<!DOCTYPE html>
<html lang="en">
<head>
<meta charset="utf-8">
<title>Wrenhill Acres Bourbon and Music Festival – Business Plan</title>
<link rel="stylesheet" href="https://fonts.googleapis.com/css2?family=Libre+Baskerville&family=Anton&family=Oswald:wght@700&display=swap">
<style>
  :root {
    --gold-deep: #b8720c;
    --gold: #d99a1c;
    --gold-light: #f0c24a;
    --green: #82ad2e;
    --green-deep: #5f8c1a;
    --green-text: #6a9720;
    --orange-line: #e8a21a;
    --white: #ffffff;
    --title-ink: #3b2810;
    --photo-sky: #dfe6e4;
    --photo-canopy: #4f6e34;
    --photo-lawn: #6f8f3e;
  }
  * { margin: 0; padding: 0; box-sizing: border-box; }
  html, body { width: 900px; height: 1200px; overflow: hidden; background: #f2f2f2; }

  .cover {
    position: relative;
    width: 900px;
    height: 1200px;
    overflow: hidden;
    background: var(--green);
  }
  .cover__header {
    position: absolute;
    inset: 0 0 auto 0;
    height: 480px;
    background: radial-gradient(ellipse at 50% 40%, var(--gold-light) 0%, var(--gold) 45%, var(--gold-deep) 100%);
  }
  .cover__title {
    position: absolute;
    top: 120px;
    left: 0;
    width: 100%;
    text-align: center;
    font-family: "Libre Baskerville", serif;
    font-size: 38px;
    line-height: 1.4;
    letter-spacing: 1px;
    text-transform: uppercase;
    color: var(--title-ink);
  }
  .cover__photo {
    position: absolute;
    top: 330px;
    left: 0;
    width: 900px;
    height: 600px;
    background:
      linear-gradient(180deg, transparent 0%, transparent 62%, var(--photo-lawn) 78%, #56762e 100%),
      radial-gradient(ellipse at 55% 35%, var(--photo-sky) 0%, #b9c6bc 22%, transparent 42%),
      linear-gradient(90deg, #3f5e2a 0%, var(--photo-canopy) 30%, #7f9560 50%, var(--photo-canopy) 70%, #3a5826 100%);
  }
  .cover__waves {
    position: absolute;
    inset: 0;
    width: 900px;
    height: 1200px;
  }
  .plan-label {
    position: absolute;
    top: 930px;
    left: 120px;
    width: 660px;
    height: 96px;
    background: var(--white);
    box-shadow: 0 3px 6px rgba(0,0,0,0.25);
    display: flex;
    align-items: center;
    justify-content: center;
    font-family: "Anton", sans-serif;
    font-size: 66px;
    letter-spacing: 1px;
    color: var(--green-text);
    text-transform: uppercase;
  }
  .prepared {
    position: absolute;
    top: 1048px;
    left: 0;
    width: 100%;
    text-align: center;
    font-family: "Oswald", sans-serif;
    font-weight: 700;
    font-size: 30px;
    line-height: 1.3;
    color: var(--white);
    text-shadow: 0 2px 3px rgba(0,0,0,0.3);
  }
</style>
</head>
<body>
  <main class="cover">
    <div class="cover__header"></div>
    <div class="cover__photo" role="img" aria-label="Photograph of the historic brick manor house at Wrenhill Acres framed by tall trees and a white fence on a green lawn"></div>

    <svg class="cover__waves" viewBox="0 0 900 1200" aria-hidden="true">
      <!-- top swoosh -->
      <path d="M0 470 C 260 380, 560 330, 900 300 L 900 0 L 0 0 Z" fill="var(--gold)" opacity="0"/>
      <path d="M0 440 C 250 400, 520 350, 900 310 L 900 280 C 560 310, 260 360, 0 410 Z" fill="var(--white)"/>
      <path d="M0 460 C 250 410, 520 370, 900 330 L 900 310 C 520 350, 250 400, 0 440 Z" fill="var(--green)"/>
      <path d="M0 500 C 200 450, 420 420, 650 400 C 480 420, 230 460, 0 540 Z" fill="var(--white)"/>
      <!-- bottom swoosh -->
      <path d="M0 880 C 300 840, 600 820, 900 800 L 900 808 C 600 830, 300 852, 0 892 Z" fill="var(--orange-line)"/>
      <path d="M0 892 C 300 852, 600 830, 900 808 L 900 850 C 600 862, 300 885, 0 925 Z" fill="var(--white)"/>
      <path d="M0 925 C 300 885, 600 862, 900 850 L 900 1200 L 0 1200 Z" fill="var(--green)"/>
      <path d="M0 1200 L 0 1120 C 300 1150, 600 1140, 900 1080 L 900 1200 Z" fill="var(--green-deep)" opacity="0.35"/>
    </svg>

    <h1 class="cover__title">Wrenhill Acres Bourbon<br>and Music Festival</h1>

    <div class="plan-label">Business Plan</div>
    <p class="prepared">Prepared By:<br>Dana Whitlock</p>
  </main>
</body>
</html>
```